Harbor Wings is an innovative offering which enables the mass market to book seats on private jets at commercial airline prices to destinations worldwide.

We need a lgog and Wordpress theme header for this initiative. Will like need other matrials but need these two images asap

```html
<!DOCTYPE html>
<html lang="en">
<head>
<meta charset="utf-8">
<title>Harbor Wings</title>
<link href="https://fonts.googleapis.com/css2?family=Arimo:wght@400;700&family=Josefin+Sans:wght@300;400&display=swap" rel="stylesheet">
<style>
:root{
  --navy-deep:#0b1f55;
  --navy:#163a86;
  --navy-mid:#1f4fa3;
  --sky-pale:#dcefff;
  --sky-light:#eef7ff;
  --panel-edge:#9ec6ea;
  --text-navy:#1c2a66;
  --heading-red:#d4141c;
  --link-orange:#e89a10;
  --frame-pink:#c2447e;
  --white:#ffffff;
}
*{margin:0;padding:0;box-sizing:border-box}
html,body{width:1200px;height:980px;overflow:hidden}
body{
  position:relative;
  font-family:"Arimo",Arial,sans-serif;
  color:var(--text-navy);
  background:linear-gradient(180deg,var(--navy-deep) 0px,var(--navy) 120px,var(--navy-mid) 460px,#2a62b8 980px);
}
.site-frame{position:absolute;left:38px;top:112px;width:1125px;height:818px;background:var(--navy-deep)}
.content-area{position:absolute;left:44px;top:443px;width:1113px;height:487px;
  background:linear-gradient(180deg,#d9ecfb 0,var(--white) 70px)}
.footer{position:absolute;left:0;top:930px;width:1200px;height:50px;
  background:linear-gradient(180deg,#d8f0fb,#eaf7fd);text-align:center;
  font-size:14.5px;line-height:46px;color:var(--text-navy)}

.utility-links{position:absolute;left:926px;top:14px;font-size:16px;color:var(--white);white-space:nowrap}
.utility-links span{margin:0 5px}

.brand{position:absolute;left:46px;top:54px;display:flex;align-items:center;gap:12px;white-space:nowrap}
.brand-dot{width:14px;height:14px;border-radius:50%;background:#8fc4f2}
.brand-name{font-family:"Josefin Sans",sans-serif;font-weight:300;font-size:33px;
  letter-spacing:4px;color:#8fc4f2;text-transform:uppercase;line-height:1}

.main-nav{position:absolute;top:76px;left:0}
.main-nav a{position:absolute;top:0;height:32px;line-height:32px;text-align:center;white-space:nowrap;
  color:var(--white);font-size:16.5px;text-decoration:none;
  background:linear-gradient(180deg,#4f86d6 0,#2a5eb6 50%,#1b4596 100%);
  border-top:1px solid #8ab3ea}

.login-panel{position:absolute;left:44px;top:115px;width:259px;height:324px;
  background:linear-gradient(180deg,#d2e9fb,#f3f9ff 40%,var(--white));padding:14px 16px}
.login-panel h2{font-size:23px;font-weight:400;color:var(--heading-red);margin:0 0 10px 4px}
.login-panel label{display:block;font-size:16.5px;font-weight:700;color:var(--text-navy);margin-left:4px}
.field{width:223px;height:24px;border:1px solid #7a8aa0;background:var(--white);
  margin:12px 0 20px 4px;border-radius:2px}
.login-btn{margin:0 0 0 96px;width:127px;height:32px;color:var(--white);font-size:19px;
  text-align:center;line-height:32px;background:linear-gradient(180deg,#5d8fd8,#1b3f8c)}
.remember{font-size:15px;margin:16px 0 0 0;display:flex;align-items:center;gap:7px;white-space:nowrap}
.remember i{width:13px;height:13px;border:1px solid #888;background:var(--white);display:block}
.login-links{font-size:14.5px;margin:10px 0 0 20px;white-space:nowrap}
.login-links span{margin-right:10px}

.hero{position:absolute;left:313px;top:115px;width:844px;height:324px;
  background:linear-gradient(180deg,#8b2d7a,var(--frame-pink));padding:16px 15px 14px}
.hero-photo{width:100%;height:100%;position:relative;
  background:linear-gradient(180deg,#b9ddf6 0,#e8f5fd 45%,#a9d0f0 100%)}
.hero-title{position:absolute;left:16px;bottom:22px;font-family:"Josefin Sans",sans-serif;
  font-weight:300;font-size:33px;letter-spacing:2px;color:#1c3378;text-transform:uppercase;white-space:nowrap}

.side-box{position:absolute;left:44px;width:259px;
  background:linear-gradient(180deg,#eaf5fe,#d6ebfb);border:1px solid var(--panel-edge)}
.side-box h3{font-weight:400;color:var(--text-navy);white-space:nowrap}
.side-box p{font-size:15px;line-height:22.5px;color:var(--text-navy);overflow:hidden}
.thumb{position:absolute;border:1px solid #b8cde0}
.more{position:absolute;right:16px;bottom:4px;font-size:15px;color:var(--link-orange)}

.story{position:absolute;left:315px;top:455px;width:838px;font-size:15.6px;line-height:23.4px;color:var(--text-navy)}
.story p{margin-bottom:23.4px}
</style>
</head>
<body>
<div class="site-frame"></div>
<div class="content-area"></div>

<nav class="utility-links">Home<span>|</span>Careers<span>|</span>Contact us</nav>

<div class="brand">
  <div class="brand-dot"></div>
  <div class="brand-name">Harbor Wings</div>
</div>

<nav class="main-nav">
  <a style="left:415px;width:124px">About us</a>
  <a style="left:548px;width:136px">Charter Service</a>
  <a style="left:690px;width:128px">Aircraft Sales</a>
  <a style="left:825px;width:125px">Maintenance</a>
  <a style="left:957px;width:175px">Aircraft Investment</a>
</nav>

<aside class="login-panel">
  <h2>Log-In Now</h2>
  <label>User Name :</label>
  <div class="field"></div>
  <label>Password :</label>
  <div class="field"></div>
  <div class="login-btn">Login</div>
  <div class="remember"><i></i>Remember my username</div>
  <div class="login-links"><span>Signup Now</span>Forgot Password</div>
</aside>

<section class="hero">
  <div class="hero-photo" role="img" aria-label="Private jet flying above a bright sea of clouds">
    <div class="hero-title">Plane Conversation</div>
  </div>
</section>

<section class="side-box" style="top:449px;height:141px">
  <div class="thumb" role="img" aria-label="Globe with flight routes icon" style="left:6px;top:20px;width:80px;height:78px;background:radial-gradient(circle at 45% 45%,#5fb0f0,#1d5fb8 60%,#f4f9ff 62%)"></div>
  <h3 style="position:absolute;left:95px;top:20px;font-size:20px">Our Network</h3>
  <p style="position:absolute;left:95px;top:52px;width:150px">View our latest routes and connections</p>
  <div class="more">more....</div>
</section>

<section class="side-box" style="top:605px;height:138px">
  <div class="thumb" role="img" aria-label="Newspaper icon" style="left:6px;top:16px;width:80px;height:78px;background:linear-gradient(180deg,#cfe8c8,#7fb36f)"></div>
  <h3 style="position:absolute;left:102px;top:16px;font-size:20px">Latest News</h3>
  <p style="position:absolute;left:99px;top:45px;width:152px;height:68px">Guests are requested to report early for check-in to complete</p>
  <div class="more" style="background:#e2f0fc;padding-left:4px">more....</div>
</section>

<section class="side-box" style="top:760px;height:141px">
  <h3 style="position:absolute;left:8px;top:4px;font-size:20px">Charter Services</h3>
  <div class="thumb" role="img" aria-label="Private jet in flight" style="left:8px;top:32px;width:158px;height:74px;background:linear-gradient(180deg,#ffffff,#e4ecf4)"></div>
  <p style="position:absolute;left:170px;top:32px;width:80px">When time and produ-ctivity</p>
  <div class="more">more....</div>
</section>

<main class="story">
  <p>In 1982, Harbor Wings began as an air charter firm with one plane and one employee. Over the past quarter century ground support, in house maintenance, aircraft sales and infrastructure development were added to our service portfolio. Along the way we built a team of highly skilled and experienced professionals. All of us are dedicated to delivering Platinum Quality products and services for our customers 24/7</p>
  <p>In 1991 Harbor Wings began donating time and resources to non profit groups in the Bayside Region. Managers and employees sponsored a Pathfinders Troop, participated in a community leadership development program and served on the chamber of commerce and Little Explorers House Boards. The company donates the use of its Eastport FBO hanger for the Youth Harbor Club annual fundraiser.</p>
  <p>Hands On Learning is showcased in our most visible outreach efforts. Harbor Wings mechanics designed and built a child sized full motion flight simulator in 1991. More than 300,000 young pilots have earned their wings at its controls. Building this machine led to Summit Air being chosen to restore and modify a Skylark 150 for interactive display in the Coastal Aviation Museum in Harborview. Since the exhibit opened in September 1996, over 10 million kids (and kids at heart) have experienced the thrill of being at the controls. Harbor Wings continues to maintain both of these interactive exhibits.</p>
</main>

<footer class="footer">© copyright 2010 Harbor Wings All Rights Reserved</footer>
</body>
</html>
```